Launch of Plovanta.com

Need a banner ad for the launch of a new website that covers Singapore, Australia and India. The website is www.plovanta.com (the Singapore one is www.plovanta.com.sg and the India one is www.plovanta.in). Note that all three are english speaking countries and the ad need to be in english.

The value proposition are :

a. It has all job listings available in the country and many times larger the nearest competitor job listing.
b. You can find almost any job you want in the country, kinda of infinite choices for you.
c. It is the coolest and hippest jobs search site.
(Avoid green and orange as they are the competitors' colors)
Updates

Project Deadline Extended
Reason: Some of the designs have come in pretty good, but need some touch up. I have given the feedback and appreciate the need to time to change.

Project Deadline Extended
Reason: I realised that the tagline that I guided you looks and sounds awful. I am making some changes and will revert to you. Sorry.

Target Market(s)

Mass market

Requirements
Must have
• Be daring in the statement, be bold in trying out use of pictures or graphics that is controversial or suggestive, as long it is not porn.
Should not have
• Premium look, or appeal only to the professional .

```html
<!DOCTYPE html>
<html lang="en">
<head>
<meta charset="utf-8">
<title>Plovanta launch banners</title>
<link rel="stylesheet" href="https://fonts.googleapis.com/css2?family=Arimo:wght@400;700&display=swap">
<style>
:root{
  --page:#ffffff;
  --ink:#3a3a3a;
  --label:#444444;
  --sky:#2a9ee0;
  --sky-deep:#1b7fc6;
  --sky-light:#5cc0f2;
  --accent:#8a45c4;
  --accent-deep:#6a2aa3;
  --accent-light:#b27ae0;
  --accent-edge:#5d2391;
  --cta:#e2336f;
  --cta-light:#f2638f;
  --cta-edge:#b81f55;
  --headline-ink:#ffffff;
  --headline-hi:#ffe36b;
  --panel:#eef4f8;
  --panel-edge:#9fc2d8;
  --field:#ffffff;
  --logo:#2f8fcf;
  --cream:#f6e2b0;
  --photo-a:#d9d9d9;
  --photo-b:#2b2b2f;
}
*{box-sizing:border-box;margin:0;padding:0}
html,body{width:1200px;height:1200px;overflow:hidden;background:var(--page)}
body{font-family:"Arimo",Arial,sans-serif;color:var(--ink)}
.stage{position:absolute;left:0;top:0;width:850px;height:850px;transform:scale(1.41176);transform-origin:0 0}
.banner{position:absolute;overflow:hidden;border:1px solid #8a8a8a;background:var(--sky)}
.size-label{position:absolute;font-size:15px;color:var(--label);letter-spacing:.3px}
.bg-sky{position:absolute;inset:0;background:linear-gradient(180deg,var(--sky-deep),var(--sky) 45%,var(--sky-light))}
.curve{position:absolute}
.brand{position:absolute;font-weight:400;color:var(--logo);letter-spacing:-.5px;white-space:nowrap}
.categories{position:absolute;color:#fff;text-align:center;line-height:1.2;white-space:nowrap}
.headline{position:absolute;background:linear-gradient(180deg,var(--accent-light),var(--accent) 50%,var(--accent-deep));border:1px solid var(--accent-edge);border-radius:3px;text-align:center;font-weight:700;color:var(--headline-ink);line-height:1.1;white-space:nowrap}
.headline .hi{color:var(--headline-hi)}
.photo{position:absolute;background:linear-gradient(180deg,var(--photo-a) 0%,#bfbfbf 35%,var(--photo-b) 100%)}
.search{position:absolute;background:linear-gradient(180deg,#f7fbfd,var(--panel));border:1px solid var(--panel-edge);border-radius:3px}
.field-label{position:absolute;font-size:11px;color:#333}
.field{position:absolute;background:var(--field);border:1px solid #b8c6cf;border-radius:3px;font-size:7.5px;color:#333;padding-left:6px;display:flex;align-items:center;white-space:nowrap;overflow:hidden}
.btn{position:absolute;background:linear-gradient(180deg,var(--cta-light),var(--cta));border:1px solid var(--cta-edge);border-radius:3px;color:#fff;font-size:11px;display:flex;align-items:center;justify-content:center}
.cream{position:absolute;background:linear-gradient(180deg,var(--cream),#fff6e2)}
</style>
</head>
<body>
<div class="stage">

  <!-- Leaderboard 728x90 -->
  <div class="banner leaderboard" style="left:55px;top:35px;width:727px;height:89px">
    <div class="bg-sky"></div>
    <div class="photo" role="img" aria-label="Photo of a smiling man and woman in business suits" style="left:165px;top:0;width:135px;height:89px"></div>
    <svg class="curve" style="left:0;top:0" width="230" height="89" viewBox="0 0 230 89">
      <path d="M0 0H205Q228 44 205 89H0Z" fill="var(--accent)"/>
      <path d="M0 0H192Q214 44 192 89H0Z" fill="#ffffff"/>
    </svg>
    <div class="brand" style="left:14px;top:22px;font-size:30px">Plovanta</div>
    <div class="categories" style="left:300px;top:1px;width:427px;font-size:11.5px">Part Time, Admin, Temp, Marketing, Acccounting</div>
    <div class="headline" style="left:273px;top:18px;width:448px;height:30px;font-size:14px;padding-top:7px">Nora and Neil Found <span class="hi">GREAT JOBS!</span></div>
    <div class="search" style="left:292px;top:52px;width:435px;height:33px;border-radius:0"></div>
    <div class="field-label" style="left:298px;top:62px">What</div>
    <div class="field" style="left:329px;top:57px;width:134px;height:23px">Job tittle, company, keywods</div>
    <div class="field-label" style="left:466px;top:62px">Where</div>
    <div class="field" style="left:503px;top:57px;width:134px;height:23px">e.g.Sidney, Peth ot Melboune</div>
    <div class="btn" style="left:643px;top:57px;width:71px;height:23px">Search</div>
  </div>
  <div class="size-label" style="left:53px;top:132px">728X90&nbsp; 26.0KB</div>

  <!-- Medium rectangle 300x250 -->
  <div class="banner rectangle" style="left:53px;top:219px;width:300px;height:250px">
    <div class="bg-sky"></div>
    <div class="cream" style="left:0;top:178px;width:20px;height:72px"></div>
    <svg class="curve" style="left:0;top:0" width="300" height="50" viewBox="0 0 300 50">
      <path d="M0 0H300V44Q150 32 0 44Z" fill="var(--accent)"/>
      <path d="M0 0H300V38Q150 26 0 38Z" fill="#ffffff"/>
    </svg>
    <div class="brand" style="left:82px;top:6px;font-size:28px">Plovanta</div>
    <div class="categories" style="left:0;top:55px;width:300px;font-size:11.5px">Part Time, Admin, Temp, Marketing, Accounting</div>
    <div class="photo" role="img" aria-label="Photo of a smiling man and woman in business suits" style="left:163px;top:75px;width:137px;height:175px"></div>
    <div class="headline" style="left:15px;top:73px;width:200px;height:52px;font-size:15px;padding-top:6px">Nora and Neil Found<br><span class="hi" style="font-size:18px">GEAT JOBS!</span></div>
    <div class="search" style="left:15px;top:126px;width:146px;height:124px"></div>
    <div class="field-label" style="left:40px;top:133px">What</div>
    <div class="field" style="left:35px;top:147px;width:118px;height:25px">Job tittle, company, keywods</div>
    <div class="field-label" style="left:40px;top:176px">Where</div>
    <div class="field" style="left:35px;top:189px;width:118px;height:25px">e.g.Sidney, Peth ot Melboune</div>
    <div class="btn" style="left:50px;top:220px;width:86px;height:22px">Seach Now</div>
  </div>
  <div class="size-label" style="left:53px;top:478px">300X250&nbsp; 30.4KB</div>

  <!-- Skyscraper 160x600 -->
  <div class="banner skyscraper" style="left:620px;top:166px;width:160px;height:600px">
    <div class="bg-sky"></div>
    <div class="cream" style="left:0;top:395px;width:160px;height:30px"></div>
    <svg class="curve" style="left:0;top:0" width="160" height="115" viewBox="0 0 160 115">
      <path d="M0 0H160V100Q80 86 0 104Z" fill="var(--accent)"/>
      <path d="M0 0H160V94Q80 80 0 98Z" fill="#ffffff"/>
    </svg>
    <div class="brand" style="left:6px;top:32px;font-size:31px">Plovanta</div>
    <div class="categories" style="left:4px;top:120px;width:152px;font-size:13px">Part Time, Admin,<br>Temp, Marketing,<br>Accounting</div>
    <div class="headline" style="left:12px;top:176px;width:136px;height:98px;font-size:16px;padding-top:16px">Nora &amp; Neil<br>Found<br><span class="hi">GREAT JOBS!</span></div>
    <div class="search" style="left:12px;top:286px;width:135px;height:140px"></div>
    <div class="field-label" style="left:27px;top:293px">What</div>
    <div class="field" style="left:20px;top:308px;width:120px;height:27px">Job tittle, company, keywods</div>
    <div class="field-label" style="left:27px;top:341px">Where</div>
    <div class="field" style="left:20px;top:356px;width:120px;height:27px">e.g.Sidney, Peth ot Melboune</div>
    <div class="btn" style="left:35px;top:391px;width:88px;height:25px">Seach Now</div>
    <div class="photo" role="img" aria-label="Photo of a smiling man and woman in business suits" style="left:0;top:425px;width:160px;height:175px"></div>
  </div>
  <div class="size-label" style="left:628px;top:777px">160X600&nbsp; 33.9KB</div>

</div>
</body>
</html>
```